Design a cool print brochure for an NGO / Give your work a global impact!!

Hi,
I provide a full design brief (below, please scroll) and a mood board (attached) to help you visualize inside my head.. ;-)
I am also available to help and have worked many years in advertising; we will understand each other.
Objective:
To design an A4 folded in two presentation brochure for a non-profit consulting agency called Mer-ova.
Mer-ova works in sustainability and international development = working with NGO’s, governments and private sector on global issues such as global warming, education for all etc.
Strategy:
This document is a first step in developing a communication strategy. It will be distributed during a major international event called the Brenvik Outreach Forum.
Objective:
The double objective of the brochure is:
a) to inform the recipient of what Mer-ova is, in the shortest time possible.
b) to showcase relevant projects to demonstrate Mer-ova experience and expertise.
Target:
Main target:
Existing Mer-ova contacts, such as members of development organizations, NGOs, private sector foundations (CSR), regional networks and other development actors.
NB: the main target already has a certain awareness of Mer-ova: we will try to minimize text to maximize visual impact and readability.
Secondary target:
Mer-ova will also distribute the brochure to new prospects of interest during the Brenvik Forum.
Timing:
We will need to finalize the design and have the files by June 1st to allow time for print before the event.
Content:
The document should be concise, highly readable (no clutter) and include:
1. text (that we will provide)
and
2. visual elements such as images, shapes and info-graphics (that is you).
NB: Mer-ova does not have its own image bank; photos will be provided by you.
Format:
A4 folded in half - 4pp A5 - PORTRAIT FORMAT) with an impactful visual in the front, logo, title and headline (please see examples in the mood board attached).
Design elements:
Mer-ova does not have yet a visual identity (please see: http://mer-ova.org) so there is room for creativity and no graphic chart to follow.
The sector of consulting in international development is rather conservative but our intention is to be disruptive and create a “Wow” effect. We count on you for that!
Therefore, the design should be “structured”, “organized”, “uncluttered” but also “modern”, “impactful”, “highly visual” (think infographic or mind map to describe our services and projects).
Please, take the time to see the attached presentation: I give you guidelines and examples of what we want and what we like.
We are looking forward to seeing your work and I am available for comments, questions and support.
Thank you.
RM
Target Market(s)
The full brief is in the project description: please, scroll through it.
The target market is : our existing clients base, working in sustainable development (read: NGO and Concord Assembly people)
Industry/Entity Type
Ngo
Requirements
Must have
- - Design and color elements: please, no black and white. Our company website is in black and white and without graphics; we want the brochure to break away from that and start creating our brand identity; so please, show us colors and desing elements (shapes, backgrounds, etc).
- You have a chance to showcase your talent in terms of visual identity: what lines, forms, layout and colors can you come up with and apply throughout the brochure and serve as the visual identity of Mer-ova?
- The structure of the document should be:
- - Front cover: design elements + impacful photo (see mood board example attached) +our logo + this headline: "Collective action for sustainable development and impact"
- - Inside front: a graphic representation of "Our Services": such as core activity in the center circle and satellite circles for the services we offer.
- - Inside back:
- 1. Icons and text boxes for "Our projects"
- 2. A world map of the countries where we have worked. Full list of countries is here:
- http://mer-ova.org/experience-1
- - Back cover: our contact + logos of partners.
- Our partners are listed here:
- Please use their original logos (ie, in color).
- The design we will select will serve as a basis for a graphic chart...so more work to come...word to the wise ;)
- Please check out our website mer-ova.org to see what we do etc.
Nice to have
- Icons to reflect our services: what icons can you come up with to describe "training services", "building networks" or "program management"?
- I give examples in the mood board.
Should not have
- We are open to creativity and want to generate a "Wow" effect.
- Just note that the sector is rather conservative so flashy colors and cartoon like characters should be avoided. Think "earth, global change, Concord Assembly, climate" without going too green (it's overdone). ;-)
- Make us stand out in the NGO world
- Now you.

```html
<!DOCTYPE html>
<html lang="en">
<head>
<meta charset="utf-8">
<title>Mer-ova — Our Services &amp; Our Presence</title>
<link href="https://fonts.googleapis.com/css2?family=Bebas+Neue&family=Roboto+Condensed:wght@300;400&display=swap" rel="stylesheet">
<style>
  :root {
    --teal: #22a896;
    --lime: #a8cc3a;
    --lime-soft: #d3e07c;
    --orange: #f19b58;
    --peach: #f6ac7e;
    --cream: #f4dca0;
    --sage: #a9a97c;
    --white: #ffffff;
    --map-pink: #d9589a;
    --map-cream: #f4d5b5;
  }
  * { margin: 0; padding: 0; box-sizing: border-box; }
  html, body { width: 1200px; height: 848px; overflow: hidden; background: var(--teal); }
  .spread { position: relative; width: 1200px; height: 848px; background: var(--teal); overflow: hidden; font-family: "Roboto Condensed", sans-serif; }

  .top-tab { position: absolute; left: 0; top: 0; width: 532px; height: 35px; background: var(--lime); border-bottom-right-radius: 35px; }
  .fold-band { position: absolute; left: 596px; top: 0; width: 36px; height: 848px; background: var(--lime); border-radius: 36px 0 0 36px; }

  .section-title { position: absolute; font-family: "Bebas Neue", sans-serif; color: var(--lime); font-size: 58px; line-height: 1; white-space: nowrap; }
  .title-services { left: 194px; top: 70px; }
  .title-projects { left: 640px; top: 70px; }
  .title-presence { left: 644px; top: 532px; }

  .intro { position: absolute; left: 90px; top: 133px; width: 442px; font-size: 7.4px; line-height: 8.4px; color: var(--lime-soft); text-align: center; text-transform: uppercase; font-weight: 300; }

  .graphics { position: absolute; left: 0; top: 0; }

  .core { position: absolute; left: 68px; top: 266px; width: 200px; text-align: center; font-family: "Bebas Neue", sans-serif; line-height: 1; }
  .core .l1 { font-size: 35px; color: var(--peach); }
  .core .l2 { font-size: 22px; color: var(--cream); margin-top: 1px; }
  .core .l3 { font-size: 30px; color: var(--cream); }
  .core .l4 { font-size: 22px; color: var(--cream); margin-top: 2px; }
  .core .l5 { font-size: 30px; color: var(--orange); margin-top: 2px; }
  .core .hot { color: var(--orange); }
  .core .peach { color: var(--peach); }
  .core .small { font-size: 22px; }
  .core .mid { font-size: 28px; }

  .service { position: absolute; font-family: "Bebas Neue", sans-serif; color: var(--orange); font-size: 17px; line-height: 20px; text-align: center; white-space: nowrap; }
  .service::after { content: ""; display: block; height: 4px; border-radius: 2px; background: var(--lime); margin: 1px auto 0; width: var(--bar); }
  .svc-research { left: 382px; top: 288px; --bar: 132px; }
  .svc-facilitation { left: 386px; top: 436px; --bar: 132px; }
  .svc-evaluation { left: 382px; top: 572px; --bar: 92px; }
  .svc-coalition { left: 336px; top: 736px; --bar: 154px; }
  .svc-training { left: 86px; top: 535px; --bar: 118px; }
  .svc-methods { left: 48px; top: 695px; --bar: 120px; }

  .region { position: absolute; font-family: "Bebas Neue", sans-serif; color: var(--white); font-size: 34px; line-height: 1; white-space: nowrap; }
  .region-europe { left: 992px; top: 537px; }
  .region-asia { left: 1102px; top: 537px; }
  .region-america { left: 646px; top: 614px; }
  .region-africa { left: 646px; top: 725px; }

  .countries { position: absolute; font-size: 6.6px; line-height: 8.4px; color: var(--white); text-align: right; text-transform: uppercase; font-weight: 300; white-space: nowrap; }
  .countries-europe { left: 960px; top: 572px; width: 112px; }
  .countries-asia { left: 1088px; top: 572px; width: 60px; }
  .countries-america { left: 630px; top: 650px; width: 110px; }
  .countries-africa { left: 630px; top: 762px; width: 90px; }

  .world-map { position: absolute; left: 760px; top: 628px; width: 384px; height: 176px; background: linear-gradient(100deg, var(--map-pink) 0%, var(--map-pink) 40%, var(--map-cream) 52%, var(--map-pink) 68%, var(--map-cream) 84%, var(--map-pink) 100%); opacity: 0.9; clip-path: polygon(0 0, 206px 0, 206px 40px, 100% 40px, 100% 100%, 0 100%); }
</style>
</head>
<body>
<main class="spread">
  <div class="top-tab"></div>
  <div class="fold-band"></div>

  <h1 class="section-title title-services">OUR SERVICES</h1>
  <h2 class="section-title title-projects">OUR PROJECTS</h2>
  <h2 class="section-title title-presence">OUR PRESENCE</h2>

  <p class="intro">Mer-ova specializes in the analysis of multi-actor cooperation and the facilitation of processes of change. We believe in the need to improve both the understanding and use of collaborative action. For that, we support value-oriented organisations to integrate a better cooperation logic in their daily practice, whether as part of the internal management process or in the context of their relations with other stakeholders. We see our clients as our most important partners. Through them we learn and improve our knowledge about the challenges of collaborative action. That’s why listening carefully to our clients’ needs and views is a critical step before designing our interventions. We avoid prefabricated solutions. On the contrary, we engage with them in order to find the right solutions that respond to the needs of the organisation and the requirements of each assignment.</p>

  <svg class="graphics" width="1200" height="848" viewBox="0 0 1200 848" fill="none">
    <g stroke="var(--lime)" stroke-width="1" stroke-dasharray="5 4">
      <path d="M296 208 L240 252"/>
      <path d="M296 208 L380 268"/>
      <path d="M240 432 L396 438"/>
      <path d="M272 512 L376 564"/>
      <path d="M220 440 L344 732"/>
      <path d="M182 448 L206 528"/>
      <path d="M80 416 L24 544 L64 688"/>
    </g>
    <g stroke="var(--white)" stroke-width="1" stroke-dasharray="5 4">
      <path d="M732 616 L732 594 L846 594 L846 628"/>
      <path d="M724 750 L746 750 L746 818 L950 818 L950 804"/>
      <path d="M986 564 L972 564 L972 668"/>
      <path d="M1152 566 L1166 566 L1166 818 L1016 818 L1016 804"/>
    </g>

    <circle cx="168" cy="328" r="92" stroke="var(--orange)" stroke-width="1.2"/>
    <path d="M258 260 A118 118 0 0 1 250 422" stroke="var(--sage)" stroke-width="11"/>
    <path d="M140 224 A108 108 0 0 0 78 388" stroke="var(--sage)" stroke-width="5"/>

    <g stroke="var(--lime)" stroke-width="2" stroke-linecap="round" stroke-linejoin="round">
      <circle cx="476" cy="264" r="26"/>
      <path d="M498 276 L528 284 L526 288 L496 281"/>
      <circle cx="528" cy="424" r="7"/>
      <rect x="521" y="398" width="14" height="16" rx="2"/>
      <rect x="521" y="434" width="14" height="16" rx="2"/>
      <rect x="500" y="417" width="16" height="14" rx="2"/>
      <rect x="540" y="417" width="16" height="14" rx="2"/>
      <rect x="448" y="520" width="20" height="44" rx="3"/>
      <rect x="494" y="540" width="20" height="46" rx="3"/>
      <path d="M468 548 L482 548 M474 556 L494 556"/>
      <circle cx="478" cy="552" r="5"/>
      <circle cx="398" cy="682" r="10"/><circle cx="414" cy="682" r="10"/><circle cx="430" cy="682" r="10"/>
      <path d="M384 730 L384 706 Q398 694 412 706 L412 730 Z"/>
      <path d="M400 730 L400 706 Q414 694 428 706 L428 730 Z"/>
      <path d="M416 730 L416 706 Q430 694 444 706 L444 730 Z"/>
      <circle cx="92" cy="520" r="4"/><circle cx="108" cy="500" r="5"/><circle cx="128" cy="518" r="4"/><circle cx="122" cy="480" r="4"/><circle cx="110" cy="520" r="4"/>
      <path d="M95 517 L104 504 M112 503 L124 515 M110 496 L120 484 M108 505 L110 516 M126 478 Q136 470 142 462 M142 462 L136 463 M142 462 L143 468"/>
      <path d="M206 700 L206 690 Q206 678 218 678 L238 678 M232 672 L238 678 L232 684"/>
      <path d="M250 690 L250 740 Q250 752 238 752 L214 752 M220 746 L214 752 L220 758"/>
      <path d="M200 716 L200 734 M194 728 L200 734 L206 728"/>
      <path d="M256 706 L256 700 M252 704 L256 700 L260 704"/>
    </g>
  </svg>

  <div class="core">
    <div class="l1">OUR WORK</div>
    <div class="l2">ENCOMPASSES <span class="hot">SPECIFIC</span></div>
    <div class="l3"><span class="peach">PROJECTS</span> <span class="small">AND/OR</span></div>
    <div class="l4">ORGANISATION <span class="hot mid">AS A</span></div>
    <div class="l5">WHOLE.</div>
  </div>

  <div class="service svc-research">RESEARCH AND ANALYSIS OF<br>COOPERATION SCHEMES</div>
  <div class="service svc-facilitation">FACILITATION OF<br>PROCESSES OF CHANGE</div>
  <div class="service svc-evaluation">EVALUATION OF<br>MULTI-ACTOR PROJECTS<br>AND PROGRAMS</div>
  <div class="service svc-coalition">COALITION BUILDING TO<br>ACHIEVE COLLECTIVE GOALS</div>
  <div class="service svc-training">TRAINING TO IMPROVE<br>NETWORKED ACTION</div>
  <div class="service svc-methods">METHODOLOGIES FOR<br>ORGANIZATIONAL CHANGE AND<br>CONSENSUS BUILDING</div>

  <div class="world-map" role="img" aria-label="World map highlighting the countries where Mer-ova has worked"></div>

  <div class="region region-europe">EUROPE</div>
  <div class="region region-asia">ASIA</div>
  <div class="region region-america">AMERICA</div>
  <div class="region region-africa">AFRICA</div>

  <p class="countries countries-europe">EU 28, Norway,<br>Switzerland, Turkey,<br>Montenegro, Ukraine,<br>Serbia, Moldova,<br>Armenia, Georgia and<br>Belarus.</p>
  <p class="countries countries-asia">China,<br>Vietnam,<br>Thailand,<br>Indonesia,<br>Malaysia,<br>Singapore,<br>Bangladesh,<br>Kyrgyzstan,<br>Kazakhstan<br>and<br>Myanmar.</p>
  <p class="countries countries-america">US, Canada, Guatemala, El<br>Salvador, Panama, Costa<br>Rica, Honduras, Colombia,<br>Peru, Bolivia, Brazil,<br>Argentina, Uruguay and<br>Paraguay.</p>
  <p class="countries countries-africa">South Africa,<br>Mozambique,<br>Ethiopia, Kenya,<br>Uganda, Benin,<br>Senegal, Zimbabwe,<br>Ghana, Tunisia, Egypt<br>and Libya.</p>
</main>
</body>
</html>
```